Business card for auto dealership

Looking for a clean modern design.
Would like attached logo incorporated

Industry/Entity Type

Car dealership

Contact Information for Business Card

Name, website, phone, cell, fax, email

```html
<!DOCTYPE html>
<html lang="en">
<head>
<meta charset="utf-8">
<title>Halvern Truck &amp; Auto Sales – Business Card</title>
<link rel="stylesheet" href="https://fonts.googleapis.com/css2?family=Dancing+Script:wght@700&family=Montserrat:wght@300;500&display=swap">
<style>
  :root {
    --page: #ffffff;
    --card: #00ffff;
    --ink-light: #ffffff;
    --ink-dark: #1b1b1b;
  }
  * { margin: 0; padding: 0; box-sizing: border-box; }
  html, body { width: 1200px; height: 758px; overflow: hidden; background: var(--page); }
  .card {
    position: absolute; left: 76px; top: 75px;
    width: 1050px; height: 600px;
    background: var(--card);
    font-family: "Montserrat", sans-serif;
    color: var(--ink-light);
  }
  .brand {
    position: absolute; left: 84px; top: 120px;
    font-weight: 500; color: var(--ink-light);
    line-height: 1;
  }
  .brand-name { display: block; font-size: 118px; letter-spacing: -2px; }
  .brand-tag { display: block; font-size: 25px; letter-spacing: 1px; margin: 8px 0 0 128px; }
  .holder {
    position: absolute; right: 38px; top: 318px;
    display: flex; align-items: flex-end; gap: 18px;
  }
  .holder-name {
    font-family: "Dancing Script", cursive;
    font-weight: 700;
    font-size: 44px; line-height: 1; color: var(--ink-light);
  }
  .holder-icon { width: 38px; height: 48px; }
  .divider {
    position: absolute; left: 42px; right: 39px; top: 374px;
    height: 1px; background: var(--ink-light);
  }
  .contacts {
    position: absolute; list-style: none;
    font-weight: 300; font-size: 27px; line-height: 1;
  }
  .contacts li { display: flex; align-items: center; gap: 10px; height: 28px; }
  .contacts svg { width: 28px; height: 28px; fill: var(--ink-dark); flex: none; }
  .contacts-phone { left: 70px; top: 433px; }
  .contacts-phone li:nth-child(2) { margin-top: 20px; }
  .contacts-phone li:nth-child(3) { margin-top: 16px; }
  .contacts-online { left: 570px; top: 481px; }
  .contacts-online li:nth-child(2) { margin-top: 16px; }
</style>
</head>
<body>
<main class="card">
  <h1 class="brand">
    <span class="brand-name">Halvern</span>
    <span class="brand-tag">TRUCK &amp; AUTO SALES</span>
  </h1>

  <div class="holder">
    <span class="holder-name">Dana Halvern</span>
    <svg class="holder-icon" viewBox="0 0 38 48" aria-hidden="true">
      <circle cx="19" cy="10" r="10" fill="var(--ink-dark)"/>
      <path d="M0 48 V32 Q0 22 10 22 H28 Q38 22 38 32 V48 Z" fill="var(--ink-dark)"/>
      <path d="M16 22 L19 38 L22 22 Z" fill="var(--card)"/>
    </svg>
  </div>

  <div class="divider"></div>

  <ul class="contacts contacts-phone">
    <li>
      <svg viewBox="0 0 28 28" aria-hidden="true"><path d="M2 10 Q14 1 26 10 L24 13 L19 11 V8 H9 V11 L4 13 Z"/><rect x="5" y="13" width="18" height="12" rx="2"/></svg>
      <span>555-014-3862</span>
    </li>
    <li>
      <svg viewBox="0 0 28 28" aria-hidden="true"><path d="M6 3 L10 3 L12 9 L9 11 Q12 17 17 19 L19 16 L25 18 V22 Q24 26 20 25 Q6 21 3 7 Q3 3 6 3 Z"/></svg>
      <span>555-019-6257</span>
    </li>
    <li>
      <svg viewBox="0 0 28 28" aria-hidden="true"><rect x="7" y="2" width="14" height="7"/><rect x="2" y="10" width="24" height="10" rx="2"/><rect x="7" y="17" width="14" height="9"/></svg>
      <span>555-017-9305</span>
    </li>
  </ul>

  <ul class="contacts contacts-online">
    <li>
      <svg viewBox="0 0 28 28" aria-hidden="true"><circle cx="14" cy="14" r="12"/><path d="M2 14 H26 M14 2 V26 M14 2 Q6 14 14 26 M14 2 Q22 14 14 26 M4 8 H24 M4 20 H24" stroke="var(--card)" stroke-width="1.4" fill="none"/></svg>
      <span>Halvernauto.com</span>
    </li>
    <li>
      <svg viewBox="0 0 28 28" aria-hidden="true"><path d="M1 5 H23 V13 H1 Z"/><path d="M1 5 L12 12 L23 5" stroke="var(--card)" stroke-width="1.5" fill="none"/><path d="M1 13 H14 V20 H1 Z"/><circle cx="21" cy="20" r="6"/><circle cx="21" cy="20" r="2.5" fill="none" stroke="var(--card)" stroke-width="1.5"/></svg>
      <span>dana@halvernauto.com</span>
    </li>
  </ul>
</main>
</body>
</html>
```